Hipster Hard Apple Cider - Bike / Gear / Cog Themed Label

Hard Apple Cider Label Needed:

- Looking for a retro, fun, funky, Venice Beach vibe.

- Design should incorporate bike/bicycle/wheel elements, appeal to both sexes and should be applicable to a can. (See can example in attachments).

- There should be a main brand logo that can stand alone in representing the brand and the feel of the brand. I envision a bike wheel, Sp*kes, gears, etc.

Please use brand name posted as JPG titled "Brand Name" in Attached Files:
>>> Tw*n* C*d*r

Target Market(s)

Our consumer is:
- Millennial
- Hipster
- Adventurous
- Active (biking/cycling)
- A craft beer + wine purchaser
- Unisex, veering towards masculine (65% male)

Industry/Entity Type

Wheel

Requirements
Must have
• - Bike elements that tie in the brand name (cogs, sp*kes, gears, bike frame, etc.)
• - A strong logo that can represent the brand

```html
<!DOCTYPE html>
<html lang="en">
<head>
<meta charset="utf-8">
<title>Twine Cider – Dry Hard Cider Label</title>
<link href="https://fonts.googleapis.com/css2?family=Arimo:wght@400;700&family=Oswald:wght@500&display=swap" rel="stylesheet">
<style>
  :root{
    --page:#ffffff;
    --band:#dfe2d2;
    --panel:#e8e9e1;
    --sage:#bcc0a3;
    --ink:#555555;
    --orange:#f05a28;
    --badge:#231f20;
    --rule:#a9a9a9;
    --metal:#a6a29d;
    --metal-light:#bdb9b5;
  }
  html,body{margin:0;padding:0;overflow:hidden;}
  body{width:1200px;height:848px;background:var(--page);position:relative;font-family:"Arimo",Arial,sans-serif;}

  /* can presentation */
  .can-body{position:absolute;left:0;top:0;width:1200px;height:848px;}
  .can-label{position:absolute;left:124px;top:152px;width:300px;height:536px;overflow:hidden;background:var(--panel);}
  .can-label .label-art{left:-69px;top:8px;transform:scale(.8);transform-origin:0 0;}

  /* flat label */
  .flat-label{position:absolute;left:561px;top:86px;width:547px;height:632px;overflow:hidden;}
  .flat-label .label-art{left:0;top:0;}

  .label-art{position:absolute;width:547px;height:632px;background:var(--panel);overflow:hidden;}
  .top-band{position:absolute;left:0;top:0;width:547px;height:148px;background:var(--band);}
  .tagline{position:absolute;top:14px;width:100%;text-align:center;margin:0;font-weight:700;font-size:9px;letter-spacing:.5px;color:var(--ink);}
  .gear{position:absolute;width:384px;height:384px;border-radius:50%;background:var(--sage);top:58px;}
  .gear-left{left:-145px;}
  .gear-right{left:311px;}
  .brand-mark{position:absolute;left:206px;top:84px;width:132px;height:132px;border-radius:50%;background:#f3f2ee;box-shadow:0 2px 5px rgba(0,0,0,.25);}
  .brand-disc{position:absolute;left:11px;top:11px;width:110px;height:110px;border-radius:50%;background:var(--badge);display:flex;align-items:center;justify-content:center;}
  .brand-name{margin:0;font-weight:700;font-size:13px;color:var(--orange);letter-spacing:.3px;white-space:nowrap;}
  .divider{position:absolute;left:197px;width:150px;height:12px;}
  .divider-top{top:241px;}
  .divider-bottom{top:458px;}
  .flavour{position:absolute;top:255px;left:0;width:100%;text-align:center;margin:0;font-family:"Oswald","Arial Narrow",sans-serif;font-weight:500;font-size:122px;line-height:1;color:var(--orange);transform:scaleX(.76);}
  .style-name{position:absolute;top:395px;width:100%;text-align:center;margin:0;font-weight:700;font-size:21px;color:var(--ink);letter-spacing:.4px;}
  .size,.abv{position:absolute;width:100%;text-align:center;margin:0;font-weight:700;font-size:12px;color:var(--ink);}
  .size{top:476px;}
  .abv{top:498px;}
  .skyline{position:absolute;left:112px;top:500px;width:435px;height:112px;background:linear-gradient(to bottom,rgba(188,192,163,0) 0%,var(--sage) 60%);}
  .bottom-band{position:absolute;left:0;top:610px;width:547px;height:22px;background:var(--sage);}
  .ingredients{position:absolute;top:616px;width:100%;text-align:center;margin:0;font-weight:700;font-size:9px;letter-spacing:.3px;color:var(--ink);}
  .warning{position:absolute;left:3px;top:474px;width:108px;height:136px;background:var(--panel);color:#a0a0a0;font-size:5.3px;line-height:7px;}
  .warning h4{margin:0 0 6px 4px;font-size:5.3px;font-weight:700;}
  .warning ol{margin:0;padding-left:14px;}
  .warning li{margin-bottom:6px;}
  .warning .note{text-align:center;margin:6px 0 5px;}
  .warning .maker{text-align:center;margin:0;}
</style>
</head>
<body>
  <svg class="can-body" viewBox="0 0 1200 848" aria-hidden="true">
    <ellipse cx="273" cy="722" rx="150" ry="14" fill="#e8e8e8"/>
    <path d="M124 680 L424 680 L420 702 Q273 742 128 702 Z" fill="var(--metal)"/>
    <path d="M124 156 L126 146 Q132 116 158 96 L388 96 Q414 116 420 146 L424 156 Z" fill="var(--metal-light)"/>
    <ellipse cx="273" cy="94" rx="122" ry="30" fill="var(--metal)"/>
  </svg>

  <section class="can-label">
    <div class="label-art">
      <div class="top-band"></div>
      <p class="tagline">REFRESHINGLY COOL</p>
      <div class="gear gear-left" role="img" aria-label="Large bicycle chainring illustration"></div>
      <div class="gear gear-right" role="img" aria-label="Large bicycle chainring illustration"></div>
      <div class="brand-mark"><div class="brand-disc"><p class="brand-name">TWINE CIDER</p></div></div>
      <svg class="divider divider-top" viewBox="0 0 150 12" aria-hidden="true">
        <path d="M0 6 Q35 4 64 6 M86 6 Q115 4 150 6" stroke="var(--rule)" stroke-width="2" fill="none"/>
        <polygon points="70,1 80,1 84,6 80,11 70,11 66,6" fill="#b3b3b3"/>
      </svg>
      <h1 class="flavour">DRY</h1>
      <h2 class="style-name">HARD CIDER</h2>
      <svg class="divider divider-bottom" viewBox="0 0 150 12" aria-hidden="true">
        <path d="M0 6 Q35 4 64 6 M86 6 Q115 4 150 6" stroke="var(--rule)" stroke-width="2" fill="none"/>
        <polygon points="70,1 80,1 84,6 80,11 70,11 66,6" fill="#b3b3b3"/>
      </svg>
      <p class="size">HALF PINT</p>
      <p class="abv">7.0%</p>
      <div class="skyline" role="img" aria-label="Silhouette of palm trees and beach boardwalk"></div>
      <div class="bottom-band"></div>
      <p class="ingredients">CONTAINS APPLES AND SPICE</p>
    </div>
  </section>

  <main class="flat-label">
    <div class="label-art">
      <div class="top-band"></div>
      <p class="tagline">REFRESHINGLY COOL</p>
      <div class="gear gear-left" role="img" aria-label="Large bicycle chainring illustration"></div>
      <div class="gear gear-right" role="img" aria-label="Large bicycle chainring illustration"></div>
      <div class="brand-mark"><div class="brand-disc"><p class="brand-name">TWINE CIDER</p></div></div>
      <svg class="divider divider-top" viewBox="0 0 150 12" aria-hidden="true">
        <path d="M0 6 Q35 4 64 6 M86 6 Q115 4 150 6" stroke="var(--rule)" stroke-width="2" fill="none"/>
        <polygon points="70,1 80,1 84,6 80,11 70,11 66,6" fill="#b3b3b3"/>
      </svg>
      <h1 class="flavour">DRY</h1>
      <h2 class="style-name">HARD CIDER</h2>
      <svg class="divider divider-bottom" viewBox="0 0 150 12" aria-hidden="true">
        <path d="M0 6 Q35 4 64 6 M86 6 Q115 4 150 6" stroke="var(--rule)" stroke-width="2" fill="none"/>
        <polygon points="70,1 80,1 84,6 80,11 70,11 66,6" fill="#b3b3b3"/>
      </svg>
      <p class="size">HALF PINT</p>
      <p class="abv">7.0%</p>
      <div class="skyline" role="img" aria-label="Silhouette of palm trees and beach boardwalk"></div>
      <aside class="warning">
        <h4>GOVERNMENT WARNING:</h4>
        <ol>
          <li>ACCORDING TO THE SURGEON GENERAL, WOMEN SHOULD NOT DRINK ALCOHOLIC BEVERAGES DURING PREGNANCY BECAUSE OF THE RISK OF BIRTH DEFECTS.</li>
          <li>CONSUMPTION OF ALCOHOLIC BEVERAGES IMPAIRS YOUR ABILITY TO DRIVE A CAR OR OPERATE MACHINERY, AND MAY CAUSE HEALTH PROBLEMS.</li>
        </ol>
        <p class="note">Contains sulfites</p>
        <p class="maker">Vinted + bottled by Twine Cider<br>Oakridge, CA</p>
      </aside>
      <div class="bottom-band"></div>
      <p class="ingredients">CONTAINS APPLES AND SPICE</p>
    </div>
  </main>
</body>
</html>
```